BUsiness Card

We need a unique business card design for a new aesthetic practice, Meadowlark Aesthetics & Wellness, P.A. The reverse of the card should be an appointment card.

```html
<!DOCTYPE html>
<html lang="en">
<head>
<meta charset="utf-8">
<title>Meadowlark Aesthetics &amp; Wellness – Business Card</title>
<link href="https://fonts.googleapis.com/css2?family=EB+Garamond:ital,wght@0,400;0,600;1,400&display=swap" rel="stylesheet">
<style>
  :root {
    --navy: #0f4a66;
    --navy-dark: #0b3f59;
    --teal: #4fc6b8;
    --ink: #1d2b33;
    --muted: #5a6a72;
    --paper: #ffffff;
    --backdrop: #2a2b2d;
  }
  * { box-sizing: border-box; margin: 0; padding: 0; }
  html, body { width: 1200px; height: 900px; overflow: hidden; }
  body {
    background: var(--backdrop);
    font-family: "EB Garamond", Georgia, serif;
    color: var(--ink);
    position: relative;
  }
  .card {
    position: absolute;
    width: 620px;
    height: 354px;
    background: var(--paper);
    box-shadow: 0 10px 30px rgba(0,0,0,.45);
    overflow: hidden;
  }
  .card--appointment { left: 100px; top: 40px; }
  .card--contact { left: 480px; top: 486px; }

  /* brand lockup */
  .brand { display: flex; align-items: center; gap: 10px; color: var(--navy); }
  .brand__dot { width: 22px; height: 22px; border-radius: 50%; background: var(--navy); flex: none; }
  .brand__name { font-weight: 400; letter-spacing: .5px; line-height: 1.05; }

  /* appointment side */
  .appointment { padding: 44px 60px 0; text-align: center; }
  .label {
    display: inline-block;
    background: var(--navy);
    color: #fff;
    font-size: 17px;
    letter-spacing: 1px;
    padding: 2px 12px;
    text-transform: uppercase;
  }
  .fields { margin: 22px 0 24px; font-size: 16px; text-align: left; }
  .field-row { display: flex; gap: 24px; margin-bottom: 12px; }
  .field { display: flex; flex: 1; align-items: baseline; gap: 6px; white-space: nowrap; }
  .field__line { flex: 1; border-bottom: 2px dotted var(--muted); height: 1px; transform: translateY(-3px); }
  .policy { font-size: 16px; line-height: 1.35; margin-top: 10px; }
  .appointment .brand { justify-content: center; margin-top: 26px; }
  .appointment .brand__name { font-size: 24px; }

  /* contact side */
  .card--contact .brand { position: absolute; top: 70px; left: 0; right: 0; justify-content: center; }
  .card--contact .brand__dot { width: 30px; height: 30px; }
  .card--contact .brand__name { font-size: 28px; }
  .tagline {
    position: absolute; right: 36px; top: 170px;
    font-style: italic; font-size: 18px; color: var(--navy);
    text-align: right; line-height: 1.25;
  }
  .person { position: absolute; left: 40px; top: 200px; }
  .person__name { font-size: 20px; font-weight: 600; color: var(--navy); }
  .person__title { font-size: 14px; color: var(--muted); margin-bottom: 10px; }
  .contact-list { list-style: none; font-size: 15px; }
  .contact-list li { display: flex; align-items: center; gap: 8px; margin-bottom: 3px; }
  .contact-list svg { width: 16px; height: 16px; flex: none; }
  .contact-list .web { font-weight: 600; color: var(--navy); padding-left: 24px; }
  .band { position: absolute; left: 0; bottom: 0; width: 620px; height: 60px; }
</style>
</head>
<body>

<section class="card card--appointment" aria-label="Appointment card">
  <div class="appointment">
    <span class="label">Next Appointment</span>
    <div class="fields">
      <div class="field-row">
        <div class="field">Date: <span class="field__line"></span></div>
        <div class="field">Time: <span class="field__line"></span></div>
      </div>
      <div class="field-row">
        <div class="field">Appointment For: <span class="field__line"></span></div>
      </div>
    </div>
    <span class="label">Cancellation Policy</span>
    <p class="policy">If you are unable to keep your appointment, pl provide atleast<br>2 business days notice or full visit fee will apply.</p>
    <div class="brand">
      <span class="brand__dot"></span>
      <span class="brand__name">Meadowlark Aesthetics &amp; Wellness</span>
    </div>
  </div>
</section>

<section class="card card--contact" aria-label="Business card front">
  <div class="brand">
    <span class="brand__dot"></span>
    <span class="brand__name">Meadowlark Aesthetics &amp; Wellness</span>
  </div>

  <p class="tagline">Helping clients to<br>look and feel their best!</p>

  <div class="person">
    <p class="person__name">Elena Varsh</p>
    <p class="person__title">Owner / Founder</p>
    <ul class="contact-list">
      <li>
        <svg viewBox="0 0 16 16"><circle cx="8" cy="8" r="8" fill="var(--navy)"/><path d="M5 4.5c.6-.5 1.2-.3 1.5.3l.6 1.2c.2.4 0 .8-.3 1l-.4.3c.4 1 1.1 1.7 2.1 2.1l.3-.4c.3-.3.7-.4 1-.3l1.2.6c.6.3.8.9.3 1.5-.8.9-2 .9-3.4 0-1.3-.8-2.4-1.9-3.1-3.2-.7-1.3-.7-2.4.2-3.1z" fill="#fff"/></svg>
        +1 555-014-2290
      </li>
      <li>
        <svg viewBox="0 0 16 16"><circle cx="8" cy="8" r="8" fill="var(--navy)"/><rect x="4" y="5.2" width="8" height="5.6" fill="none" stroke="#fff" stroke-width="1"/><path d="M4 5.4l4 3 4-3" fill="none" stroke="#fff" stroke-width="1"/></svg>
        elena@meadowlark-aesthetics.com
      </li>
      <li class="web">www.meadowlark-aesthetics.com</li>
    </ul>
  </div>

  <svg class="band" viewBox="0 0 620 60" aria-hidden="true">
    <path d="M0 46 L440 46 L440 60 L0 60 Z" fill="var(--teal)"/>
    <path d="M454 60 L454 44 Q454 22 476 22 L620 22 L620 60 Z" fill="var(--navy-dark)"/>
  </svg>
</section>

</body>
</html>
```